Law Firm Website

We are a small California based law firm specializing in business, corporate and litigation matters. We need to have our website redesigned. We are looking for a new and fresh look for our site, keeping in mind that we are a law firm.
What we don't want:
**the traditional "gavel" and "scales of justice" look
**anything too crazy
What we do want:
**sophisticated yet modern and fresh corporate look and feel
**samples of websites we really like:
http://www.tkrmllp.example
http://www.hollowaybrant.example/
we also like:
http://www.fentonardis.example/
http://www.qx.example/
http://www.moberly.example/
http://www.pvtr.example
http://www.npdlaw.example/
The content will be whatever is currently on our website (www.colterlawgroup.example). We will be selecting the winner based on originality and keeping the above requirements in mind. Please note that the photos that you use will be the ones that we will be using, so choose wisely because the photos will make a difference.
Target Market(s)
Corporate clients
Industry/Entity Type
Law Firm
Look and feel

```html
<!DOCTYPE html>
<html lang="en">
<head>
<meta charset="utf-8">
<title>Colter Law Group, LLP</title>
<link rel="stylesheet" href="https://fonts.googleapis.com/css2?family=Arimo:wght@400;700&display=swap">
<style>
:root{
  --blue:#0a7ad8;
  --link:#1a78c8;
  --ink:#444;
  --muted:#555;
  --page:#f4f4f4;
  --band:#e2e2e2;
  --footer:#0b0b0b;
  --white:#fff;
  --foot-muted:#8a8a8a;
}
*{box-sizing:border-box;margin:0;padding:0}
html,body{width:1028px;height:1200px;overflow:hidden}
body{position:relative;background:var(--page);font-family:"Arimo",Arial,sans-serif;color:var(--ink)}
.abs{position:absolute}
.topline{left:0;top:0;width:1028px;height:10px;background:#111}
.header{left:0;top:10px;width:1028px;height:99px;background:var(--blue)}
.brand{left:160px;top:8px;width:180px;text-align:center;color:var(--white)}
.brand-mark{display:block;width:48px;height:48px;margin:0 auto 6px;background:#cfe6fb}
.brand-name{font-size:16px;line-height:18px}
.brand-sub{font-size:8px;line-height:12px;margin-top:2px}
.phone{right:172px;top:18px;color:var(--white);font-weight:700;font-size:13px;display:flex;align-items:center;gap:4px}
.search{left:690px;top:50px;width:165px;height:28px;background:var(--white);display:flex;align-items:center;justify-content:space-between;padding:0 10px;font-size:8px;color:#999}
.hero{left:0;top:109px;width:1028px;height:359px;background:linear-gradient(180deg,#3a2f2c 0%,#4a3c36 50%,#6b5a48 78%,#3a3330 100%)}
.hero-title{left:610px;top:256px;font-size:34px;font-weight:700;color:var(--white)}
.arrow{top:272px}
.dots{left:486px;top:439px;display:flex;gap:6px}
.dots i{width:9px;height:9px;border-radius:50%;background:#ddd;display:block}
.dots i.on{background:#111;border:1px solid #ddd}
.welcome{left:172px;top:486px;width:684px;text-align:center}
.welcome h1{font-weight:400;font-size:17px;color:var(--link);line-height:20px}
.rule{position:relative;height:4px;margin:6px 0 8px;border-top:1px solid #bbb}
.rule span{position:absolute;left:296px;top:-1px;width:94px;height:4px;background:#555}
.welcome p{font-size:8.4px;line-height:16.5px;color:var(--muted)}
.welcome a{font-size:8px;color:var(--link);text-decoration:none}
.section-title{font-size:16px;font-weight:400;color:var(--link)}
.practice{left:172px;top:626px;width:685px;height:76px;display:flex;border:1px solid #ccc;background:linear-gradient(#f7f7f7,#e8e8e8)}
.practice-item{display:flex;align-items:center;gap:14px;padding-left:28px;font-size:13px;color:#222;border-right:1px solid #ccc}
.practice-item:last-child{border-right:0}
.band{left:0;top:725px;width:1028px;height:295px;background:var(--band)}
.card{top:782px;width:194px;height:216px;background:#f7f7f7;border:1px solid #ccc;padding:6px;box-shadow:0 6px 8px -4px rgba(0,0,0,.25)}
.card-photo{height:97px;border:1px solid #bbb}
.card h3{font-size:12px;color:#444;margin:11px 0 5px}
.card p{font-size:7.6px;line-height:10px;color:#555}
.card a{display:block;margin-top:8px;font-size:7px;color:#111;text-decoration:none}
.footer{left:0;top:1020px;width:1028px;height:180px;background:var(--footer)}
.foot-title{font-size:9px;font-weight:700;color:#aaa}
.foot-rule{height:2px;background:#333;margin-top:4px;position:relative}
.foot-rule span{position:absolute;left:0;top:0;width:38px;height:2px;background:#777}
.contact dt{font-size:8px;color:var(--white);margin-top:8px}
.contact dd{font-size:8px;color:var(--foot-muted);margin-top:4px;line-height:9px}
.copy{left:0;width:1028px;top:1044px;text-align:center;font-size:8px;color:var(--white)}
.social{display:flex;gap:5px;margin-top:9px}
.social i{width:13px;height:13px;border-radius:50%;background:#777;display:block}
</style>
</head>
<body>
<div class="abs topline"></div>
<header class="abs header">
  <div class="abs brand">
    <span class="brand-mark"></span>
    <div class="brand-name">Colter Law Group, LLP</div>
    <div class="brand-sub">Attorneys at Law</div>
  </div>
  <div class="abs phone">
    <svg width="11" height="13" viewBox="0 0 11 13"><path d="M2 1l2 0 1 3-1.5 1c.6 1.8 1.6 3 3 3.8L8 7.5l3 1.2v2.3c-5 .8-10-4.6-9-10z" fill="#fff"/></svg>
    555 014 7720
  </div>
  <div class="abs search">Search
    <svg width="14" height="14" viewBox="0 0 14 14"><circle cx="6" cy="6" r="4.5" fill="none" stroke="#111" stroke-width="2"/><path d="M9.5 9.5L13 13" stroke="#111" stroke-width="2"/></svg>
  </div>
</header>

<section class="abs hero" role="img" aria-label="Night photograph of a domed capitol building lit against a dark sky"></section>
<div class="abs hero-title">Corvane</div>
<svg class="abs arrow" style="left:80px" width="16" height="26" viewBox="0 0 16 26"><path d="M13 2L3 13l10 11" fill="none" stroke="#aaa" stroke-width="4"/></svg>
<svg class="abs arrow" style="left:936px" width="16" height="26" viewBox="0 0 16 26"><path d="M3 2l10 11L3 24" fill="none" stroke="#aaa" stroke-width="4"/></svg>
<div class="abs dots"><i class="on"></i><i></i><i></i></div>

<section class="abs welcome">
  <h1>Welcome to Colter Law Group, LLP</h1>
  <div class="rule"><span></span></div>
  <p>Colter Law Group, LLP provides quality legal representation to corporate as well as individual clients in the areas of business, corporate, securities, products liability, civil litigation (in State and Federal Courts), Alternative Dispute Resolution (arbitration and mediation), as well as a host of transactional matters.</p>
  <a href="#">Learn More +</a>
</section>

<h2 class="abs section-title" style="left:172px;top:592px">Practice Areas</h2>
<div class="abs practice">
  <div class="practice-item" style="width:232px">
    <svg width="52" height="34" viewBox="0 0 52 34"><circle cx="12" cy="22" r="9" fill="none" stroke="#222" stroke-width="4"/><circle cx="38" cy="13" r="10" fill="none" stroke="#222" stroke-width="4"/><path d="M18 12l10-2" stroke="#222" stroke-width="3"/></svg>
    Criminal Cases
  </div>
  <div class="practice-item" style="width:221px">
    <svg width="42" height="42" viewBox="0 0 42 42"><rect x="14" y="2" width="14" height="14" fill="#222"/><circle cx="21" cy="8" r="3" fill="#fff"/><rect x="2" y="18" width="38" height="6" fill="#222"/><rect x="2" y="24" width="38" height="16" fill="#222"/><path d="M10 27v10M17 27v10M25 27v10M32 27v10" stroke="#fff" stroke-width="3"/></svg>
    Law Magistrate
  </div>
  <div class="practice-item" style="flex:1">
    <svg width="46" height="38" viewBox="0 0 46 38"><path d="M23 1L2 11h42z" fill="#222"/><rect x="4" y="12" width="38" height="3" fill="#222"/><path d="M9 16v15M18 16v15M28 16v15M37 16v15" stroke="#222" stroke-width="5"/><rect x="2" y="32" width="42" height="5" fill="#222"/></svg>
    <span style="margin-left:36px">Courts</span>
  </div>
</div>

<div class="abs band"></div>
<h2 class="abs section-title" style="left:172px;top:744px">Services</h2>
<svg class="abs" style="left:830px;top:743px" width="28" height="14" viewBox="0 0 28 14"><path d="M10 2L4 7l6 5M18 2l6 5-6 5" fill="none" stroke="#777" stroke-width="3"/></svg>

<article class="abs card" style="left:172px">
  <div class="card-photo" role="img" aria-label="Photo of a boardroom meeting table with documents" style="background:linear-gradient(135deg,#5a4a3c,#a88d70 55%,#3e342c)"></div>
  <h3>Corporate</h3>
  <p>Lorem ipsum dolor sit amet, consectetur adipisc-ing elit. Cras consectetur orci mollis arcu dapibus blandit iaculis urna sodales. Praesent convallis nunc lectus, in interdum ligula. Fusce ac neque arcu.</p>
  <a href="#">Link to somewhere..</a>
</article>
<article class="abs card" style="left:416px">
  <div class="card-photo" role="img" aria-label="Photo of a signed business contract with a fountain pen" style="background:linear-gradient(160deg,#7a3b2a 0 12%,#e8e8e8 12%,#cfcfcf)"></div>
  <h3>Business</h3>
  <p>Lorem ipsum dolor sit amet, consectetur adipisc-ing elit. Cras consectetur orci mollis arcu dapibus blandit iaculis urna sodales. Praesent convallis nunc lectus, in interdum ligula. Fusce ac neque arcu.</p>
  <a href="#">Link to somewhere..</a>
</article>
<article class="abs card" style="left:660px">
  <div class="card-photo" role="img" aria-label="Photo of law books on a shelf" style="background:linear-gradient(90deg,#3d3a22,#6b6440 40%,#2a2616 70%,#7a3a1c)"></div>
  <h3>Litigation</h3>
  <p>Lorem ipsum dolor sit amet, consectetur adipisc-ing elit. Cras consectetur orci mollis arcu dapibus blandit iaculis urna sodales. Praesent convallis nunc lectus, in interdum ligula. Fusce ac neque arcu.</p>
  <a href="#">Link to somewhere..</a>
</article>

<footer class="abs footer"></footer>
<div class="abs contact" style="left:170px;top:1039px;width:120px">
  <div class="foot-title">Contact</div>
  <div class="foot-rule"><span></span></div>
</div>
<dl class="abs contact" style="left:192px;top:1062px;width:170px">
  <dt>Address</dt>
  <dd>Lorem ipsum dolor sit amet, consectetuer adipiscing elit.</dd>
  <dt>Phone</dt>
  <dd>0300 555 0142</dd>
  <dt style="margin-top:12px">Email</dt>
  <dd>info@corvane.example</dd>
</dl>
<svg class="abs" style="left:171px;top:1070px" width="9" height="8" viewBox="0 0 9 8"><path d="M4.5 0L0 4h1.5v4h2V5.5h2V8h2V4H9z" fill="#fff"/></svg>
<svg class="abs" style="left:171px;top:1147px" width="10" height="8" viewBox="0 0 10 8"><rect x=".5" y="1.5" width="9" height="6" fill="none" stroke="#fff"/><path d="M.5 1.5l4.5 3.5 4.5-3.5" fill="none" stroke="#fff"/></svg>
<div class="abs copy">© 2013 Colter Law Group, LLP&nbsp; All Rights Reserved</div>
<div class="abs" style="left:702px;top:1039px;width:155px">
  <div class="foot-title">Stay Connect</div>
  <div class="foot-rule"><span></span></div>
  <div class="social"><i></i><i></i><i></i><i></i></div>
</div>
</body>
</html>
```